Corporate Business Card

Very professional, Modern, Not to busy, include phone address email, website
(253) 555-0174, 61807 19th Street N, Kent, WA 98517, marcus@kestrelbayholding.com, brelvanindustries.com

Target Market(s)

Manufacturing

Industry/Entity Type

Aero, machining, manufacturing, Off road racing

Contact Information for Business Card

Phone, address email, website

```html
<!DOCTYPE html>
<html lang="en">
<head>
<meta charset="utf-8">
<title>Brelvan Industries – Business Card</title>
<link rel="stylesheet" href="https://fonts.googleapis.com/css2?family=Montserrat:wght@400;500;800&family=Michroma&display=swap">
<style>
  :root {
    --canvas: #e9eaee;
    --paper: #ffffff;
    --navy: #1f2f6e;
    --navy-deep: #233275;
    --navy-soft: #2e3e82;
    --red: #d8262c;
    --ink: #3a3a3a;
    --ink-soft: #555555;
  }
  * { margin: 0; padding: 0; box-sizing: border-box; }
  html, body { width: 1200px; height: 1200px; overflow: hidden; }
  body {
    background: var(--canvas);
    font-family: "Montserrat", sans-serif;
    position: relative;
  }
  .card {
    position: absolute;
    top: 232px;
    width: 420px;
    height: 735px;
    border-radius: 28px;
    overflow: hidden;
    box-shadow: 0 8px 24px rgba(0,0,0,.12);
  }
  .card-front { left: 150px; background: var(--paper); }
  .card-back { left: 630px; background: var(--navy-deep); }

  /* Front */
  .brand {
    position: absolute;
    top: 150px;
    left: 0; right: 0;
    text-align: center;
  }
  .brand-name {
    font-weight: 800;
    font-size: 46px;
    letter-spacing: 2px;
    color: var(--navy);
    line-height: 1;
  }
  .brand-sub {
    font-weight: 800;
    font-size: 20px;
    letter-spacing: 1px;
    color: var(--navy);
    margin-top: 10px;
  }
  .brand-rule {
    width: 200px;
    height: 2px;
    background: var(--navy);
    margin: 14px auto 0;
    transform: translateX(-70px);
  }
  .person {
    position: absolute;
    top: 372px;
    left: 0; right: 0;
    text-align: center;
  }
  .person-name {
    font-family: "Michroma", sans-serif;
    font-size: 25px;
    color: var(--red);
  }
  .person-title {
    font-size: 15px;
    color: var(--ink-soft);
    margin-top: 6px;
  }
  .divider {
    position: absolute;
    top: 446px;
    left: 48px; right: 48px;
    display: flex;
    align-items: center;
    gap: 14px;
  }
  .divider-line { flex: 1; height: 1.5px; background: var(--red); opacity: .8; }
  .icon-set { display: flex; gap: 4px; }
  .icon-set svg { width: 22px; height: 22px; display: block; }
  .contact {
    position: absolute;
    top: 482px;
    left: 0; right: 0;
    text-align: center;
    font-size: 16px;
    line-height: 1.45;
    color: var(--ink);
  }
  .accent-rule {
    position: absolute;
    top: 600px;
    left: 50%;
    width: 90px;
    height: 2px;
    margin-left: -45px;
    background: var(--red);
  }
  .address {
    position: absolute;
    top: 626px;
    left: 0; right: 0;
    text-align: center;
    font-size: 16px;
    color: var(--ink);
  }

  /* Back */
  .pattern-field {
    position: absolute;
    inset: 0;
    background: linear-gradient(135deg, var(--navy-soft) 0%, var(--navy-deep) 50%, var(--navy-soft) 100%);
  }
  .back-brand {
    position: absolute;
    top: 330px;
    left: 0; right: 0;
    text-align: center;
    color: #ffffff;
  }
  .back-brand .brand-name { color: #ffffff; font-size: 26px; }
  .back-brand .brand-sub { color: #ffffff; font-size: 12px; margin-top: 6px; }
  .back-brand .brand-rule { background: #ffffff; width: 110px; margin-top: 8px; transform: translateX(-40px); }
</style>
</head>
<body>
  <section class="card card-front">
    <div class="brand">
      <div class="brand-name">BRELVAN</div>
      <div class="brand-sub">Industries</div>
      <div class="brand-rule"></div>
    </div>

    <div class="person">
      <div class="person-name">Marcus Hale</div>
      <div class="person-title">Managing Director</div>
    </div>

    <div class="divider">
      <span class="divider-line"></span>
      <span class="icon-set">
        <svg viewBox="0 0 22 22" aria-label="Phone">
          <rect width="22" height="22" rx="4" fill="#d8262c"/>
          <path d="M7 5.5c.8 0 1.6 2 1.6 2.6 0 .6-.9 1-.9 1.5.3 1.4 2.3 3.4 3.7 3.7.5 0 .9-.9 1.5-.9.6 0 2.6.8 2.6 1.6 0 1-1.3 2-2.3 2C9.4 16 6 12.6 5 8.8c0-1 1-2.3 2-2.3z" fill="#fff"/>
        </svg>
        <svg viewBox="0 0 22 22" aria-label="Email">
          <rect width="22" height="22" rx="4" fill="#d8262c"/>
          <rect x="5" y="7" width="12" height="8.5" rx="1" fill="none" stroke="#fff" stroke-width="1.4"/>
          <path d="M5.5 7.5 11 12l5.5-4.5" fill="none" stroke="#fff" stroke-width="1.4"/>
        </svg>
        <svg viewBox="0 0 22 22" aria-label="Website">
          <rect width="22" height="22" rx="4" fill="#d8262c"/>
          <circle cx="11" cy="11" r="5.5" fill="none" stroke="#fff" stroke-width="1.3"/>
          <ellipse cx="11" cy="11" rx="2.4" ry="5.5" fill="none" stroke="#fff" stroke-width="1.1"/>
          <path d="M5.5 11h11" stroke="#fff" stroke-width="1.1"/>
        </svg>
      </span>
      <span class="divider-line"></span>
    </div>

    <div class="contact">
      <div class="contact-line">(253) 555-0174, 61807</div>
      <div class="contact-line">marcus@kestrelbayholding.com</div>
      <div class="contact-line">www.brelvanindustries.com</div>
    </div>

    <div class="accent-rule"></div>

    <div class="address">19th Street N, Kent, WA 98517</div>
  </section>

  <section class="card card-back">
    <div class="pattern-field" role="img" aria-label="Repeating brand name pattern in tonal navy"></div>
    <div class="back-brand">
      <div class="brand-name">BRELVAN</div>
      <div class="brand-sub">Industries</div>
      <div class="brand-rule"></div>
    </div>
  </section>
</body>
</html>
```